Owen Tasker Studios Business Card

Looking for a clear, modern, elegant, sharp business card that conveys a professional yet edgy image to my business as a wedding, portrait, and travel photographer. Would like something that looks vintage yet modern. Need a new business card to grow my business. We are growing the business for Wedding and Event Photography as well as fine art Photography. (Mostly Landscapes)
Updates

I’m looking through designs now but I have a new logo that i want using please.

New logo uploaded please redesign using that

PLEASE ALL DESIGNERS LOOK IN BRIEF FOR NEW LOGO

Target Market(s)

Brides, Grooms, Families with Kids, People looking for Fine Art Photography Artwork

Industry/Entity Type

Photographer

Contact Information for Business Card

Unsure

Font styles to use
Serif

Colors

Designer to choose colors to be used in the design.

Requirements
Must have
• My Website:
• http://taskerlens.examplefolio.net
• Phone:
• 323-481-5206
• Email:
• owentaskerlens@mailbox-example.net
Nice to have
• Would like a sort of shine on the printing finish.
• I like black I think it looks good on a business card.
• Can try working with my logo (png that I've attached)

```html
<!DOCTYPE html>
<html lang="en">
<head>
<meta charset="UTF-8">
<title>Owen Tasker Studios – Business Card</title>
<link rel="stylesheet" href="https://fonts.googleapis.com/css2?family=Montserrat:wght@300;400&family=Open+Sans:wght@400;600&display=swap">
<style>
  :root {
    --backdrop: #e9e7e3;
    --card-light: #ffffff;
    --card-dark: #111111;
    --ink-dark: #141414;
    --ink-light: #f4f4f4;
  }
  * { margin: 0; padding: 0; box-sizing: border-box; }
  html, body {
    width: 1064px;
    height: 1200px;
    overflow: hidden;
    background: var(--backdrop);
  }
  .canvas {
    position: relative;
    width: 1064px;
    height: 1200px;
  }
  .card {
    position: absolute;
    left: 213px;
    width: 670px;
    height: 414px;
    text-align: center;
  }
  .card--front { top: 168px; background: var(--card-light); color: var(--ink-dark); }
  .card--back  { top: 632px; background: var(--card-dark);  color: var(--ink-light); }

  .wordmark {
    position: absolute;
    left: 0;
    right: 0;
    font-family: "Montserrat", sans-serif;
    font-weight: 300;
  }
  .wordmark__name {
    display: block;
    font-size: 43px;
    line-height: 1;
    letter-spacing: 0.5px;
  }
  .wordmark__tagline {
    display: block;
    margin-top: 14px;
    font-size: 19px;
    line-height: 1;
    letter-spacing: 12px;
    padding-left: 12px;
  }
  .card--front .wordmark { top: 155px; }
  .card--back  .wordmark { top: 234px; }

  .monogram-frame {
    position: absolute;
    left: 287px;
    top: 105px;
    width: 96px;
    height: 97px;
    border: 1.5px solid var(--ink-light);
  }

  .contact {
    position: absolute;
    left: 0;
    right: 0;
    top: 328px;
    font-family: "Open Sans", sans-serif;
    font-size: 16.5px;
    line-height: 28px;
    color: var(--ink-dark);
  }
  .contact__label { font-weight: 600; }
  .contact__divider { margin: 0 6px; }
</style>
</head>
<body>
<main class="canvas">
  <section class="card card--front">
    <div class="wordmark">
      <span class="wordmark__name">OWEN TASKER</span>
      <span class="wordmark__tagline">STUDIOS</span>
    </div>
    <div class="contact">
      <p><span class="contact__label">P:</span> 323-481-5206<span class="contact__divider">|</span><span class="contact__label">E:</span> owentaskerlens@mailbox-example.net</p>
      <p><span class="contact__label">W:</span> www.taskerlens.examplefolio.net</p>
    </div>
  </section>

  <section class="card card--back">
    <div class="monogram-frame"></div>
    <div class="wordmark">
      <span class="wordmark__name">OWEN TASKER</span>
      <span class="wordmark__tagline">STUDIOS</span>
    </div>
  </section>
</main>
</body>
</html>
```